diesel mechanic business card design

stalwart diesel is a new and upcoming business we are looking for some bad ass designs to help get us started we offer 24 hour road service, off road recovery, welding and custom fabrications we are diesel mechanics so our design should be bold and eye catching flames wrenches engine parts are cool we work in an industrial environment around heavy trucks and equipment this in not a quikko slick we fix it all nothing is to big or to small the colors red and black are always a plus but we are open to anything you guys can come up with ready set go

Target Market(s)

other small business primarily trucking and transportation companys

Industry/Entity Type

Business

Contact Information for Business Card

company name Stalwert diesel truck & trailer repair / address 14 rear north benton ave taylor PA 18530 / ownersAdam DeLuccie 570-614-3385 / Curtis Vanholm 570-248-7731 E mail owenmarcotti@fieldpost.example fax 570-692-1856

Requirements
Nice to have
• industrial modern design
Should not have
• rainbows butterfly's unicorns or cupcakes

```html
<!DOCTYPE html>
<html lang="en">
<head>
<meta charset="utf-8">
<title>Stalwart Diesel – Business Card</title>
<link rel="stylesheet" href="https://fonts.googleapis.com/css2?family=Montserrat:wght@300;400;700;800&display=swap">
<style>
  :root {
    --page: #e9e6e2;
    --black: #0b0b0c;
    --black-soft: #1c1c1e;
    --red: #d0182b;
    --red-dark: #8e0d18;
    --silver: #c9c9cc;
    --silver-dark: #6e6e72;
    --white: #ffffff;
  }
  * { box-sizing: border-box; margin: 0; padding: 0; }
  html, body {
    width: 1200px; height: 1000px; overflow: hidden;
    background: var(--page);
    font-family: "Montserrat", sans-serif;
  }
  .sheet {
    width: 1200px; height: 1000px;
    display: flex; flex-direction: column; align-items: center; justify-content: center;
    gap: 24px;
  }
  .card {
    position: relative;
    width: 820px; height: 468px;
    background: radial-gradient(ellipse at 50% 35%, var(--black-soft) 0%, var(--black) 70%);
    overflow: hidden;
    box-shadow: 0 6px 18px rgba(0,0,0,.25);
  }

  /* Front */
  .front-texture {
    position: absolute; inset: 0 0 70px 0;
    background: radial-gradient(ellipse at 50% 40%, #262628 0%, rgba(20,20,22,0) 65%);
  }
  .brand {
    position: absolute; left: 0; right: 0; text-align: center;
    color: var(--white);
  }
  .brand-name {
    display: inline-flex; align-items: center; gap: 16px;
    font-weight: 800; font-size: 52px; letter-spacing: 4px; text-transform: uppercase;
    color: var(--red); white-space: nowrap;
  }
  .brand-mark {
    flex: none; width: 26px; height: 26px; border-radius: 50%; background: var(--silver);
  }
  .brand-tagline {
    margin-top: 14px;
    font-weight: 700; font-size: 17px; letter-spacing: 1.5px; text-transform: uppercase;
    color: var(--white);
  }
  .front .brand { top: 130px; }
  .front-band {
    position: absolute; left: 0; right: 0; bottom: 46px; height: 22px;
    background: linear-gradient(90deg, var(--red-dark), var(--red) 50%, var(--red-dark));
  }
  .front-band::after {
    content: ""; position: absolute; left: 0; right: 0; bottom: -3px; height: 3px;
    background: linear-gradient(90deg, var(--silver-dark), var(--silver), var(--silver-dark));
  }

  /* Back */
  .back-top { position: absolute; inset: 0 0 220px 0; }
  .back .brand { left: 44px; right: auto; width: 400px; top: 78px; text-align: center; }
  .back .brand-name { font-size: 29px; letter-spacing: 2px; gap: 10px; }
  .back .brand-mark { width: 18px; height: 18px; }
  .back .brand-tagline { font-size: 12px; margin-top: 10px; letter-spacing: 1.2px; }
  .address {
    position: absolute; left: 500px; top: 74px;
    display: flex; gap: 10px; align-items: flex-start;
    color: var(--white); font-weight: 300; font-size: 19px; line-height: 1.3;
    white-space: nowrap;
  }
  .icon {
    flex: none; width: 26px; height: 26px; border-radius: 50%;
    background: var(--white); display: flex; align-items: center; justify-content: center;
    margin-top: 1px;
  }
  .icon svg { width: 16px; height: 16px; }
  .silver-line {
    position: absolute; left: 0; right: 0; top: 242px; height: 6px;
    background: linear-gradient(90deg, var(--silver-dark), #f2f2f4 55%, var(--silver-dark));
  }
  .back-bottom {
    position: absolute; left: 0; right: 0; bottom: 0; height: 220px;
    background: linear-gradient(100deg, var(--red-dark) 0%, var(--red) 45%, var(--red) 100%);
    display: flex; justify-content: space-between; align-items: center;
    padding: 0 44px 0 50px;
    color: var(--white);
  }
  .owners { line-height: 1.18; }
  .owner-name { font-weight: 800; font-size: 30px; text-transform: uppercase; white-space: nowrap; }
  .owner-role { font-weight: 300; font-size: 28px; text-transform: uppercase; letter-spacing: 1px; }
  .contacts { list-style: none; display: flex; flex-direction: column; gap: 8px; }
  .contacts li {
    display: flex; align-items: center; gap: 10px;
    font-weight: 300; font-size: 21px; white-space: nowrap;
  }
  .contacts .icon { margin-top: 0; }
  .contacts .icon svg path, .contacts .icon svg rect { fill: var(--red); }
</style>
</head>
<body>
<main class="sheet">

  <section class="card front" aria-label="Card front">
    <div class="front-texture" role="img" aria-label="Faint engine gears decoration"></div>
    <div class="brand">
      <div class="brand-name"><span class="brand-mark"></span>Stalwart Diesel</div>
      <div class="brand-tagline">Truck &amp; Trailer Repair</div>
    </div>
    <div class="front-band"></div>
  </section>

  <section class="card back" aria-label="Card back">
    <div class="back-top"></div>
    <div class="brand">
      <div class="brand-name"><span class="brand-mark"></span>Stalwart Diesel</div>
      <div class="brand-tagline">Truck &amp; Trailer Repair</div>
    </div>
    <div class="address">
      <span class="icon">
        <svg viewBox="0 0 16 16"><path fill="#0b0b0c" d="M8 1a5 5 0 0 0-5 5c0 3.8 5 9 5 9s5-5.2 5-9a5 5 0 0 0-5-5zm0 7a2 2 0 1 1 0-4 2 2 0 0 1 0 4z"/></svg>
      </span>
      <p>14 Rear North Benton Ave<br>Taylor PA 18530</p>
    </div>
    <div class="silver-line"></div>
    <div class="back-bottom">
      <div class="owners">
        <p class="owner-name">Owen Marcotti</p>
        <p class="owner-name">Curtis Vanholm</p>
        <p class="owner-role">Owners</p>
      </div>
      <ul class="contacts">
        <li><span class="icon"><svg viewBox="0 0 16 16"><rect x="4.5" y="1" width="7" height="14" rx="1.5"/></svg></span>570-614-3385</li>
        <li><span class="icon"><svg viewBox="0 0 16 16"><rect x="4.5" y="1" width="7" height="14" rx="1.5"/></svg></span>570-248-7731</li>
        <li><span class="icon"><svg viewBox="0 0 16 16"><path d="M4 1h6v4H4zM2 6h12v6h-2v3H4v-3H2z"/></svg></span>570-692-1856</li>
        <li><span class="icon"><svg viewBox="0 0 16 16"><path d="M1 3h14v10H1zM2 4l6 5 6-5z"/></svg></span>owenmarcotti@fieldpost.example</li>
      </ul>
    </div>
  </section>

</main>
</body>
</html>
```